Aviation Maintenance & Aircraft Cleaning Website

We need a fairly simple modern sleek website . Our company does aviation maintenance , aircraft cleaning , maintenance tracking . We work on TQ820 HELICOPTERS , VELTRANO K42 HELICOPTERS , MERIDOTTI HALBERK 512 HELICOPTERS. We would like a website that can be mobile as well with future ideas that an app where you could book cleanings and maintenance . Right now the biggest thing is for our customer to see a website , be able to book our services online and see our staff . the website must be modern and clean .

Target Market(s)

Aviation maintenance , aviation cleaning ,

Logo Text

KM but 1 image unlike the one i uploaded which is two . Im open for different aviation designs

Number of Pages Required

5+ page

Font styles to use
Serif

Requirements
Must have
• Home page , Aircraft Maintenance , Aircraft Cleaning , About Us , Contact , Careers

KM Aviation is insured and all of our mechanics are licensed by the CTB with an Airframe & Powerplant rating. ( FRONT PAGE )

Home page should have a simple nice picture of a TQ820 or Veltrano K42 . My Logo as you can see seems like two logos . i would like 1 logo and made of the two if possible . (New ideas are welcome . )

Book a Cleaning Calendar should in the aircraft cleaning page . The aircraft cleaning page should have a picture of cleaning a helicopter or private jet .

Aircraft maintenance page should have a mechanic working on a helicopter . The Page should have a fast way to contact us .

We are a mobile AOG team who is available 24/7 . What we do
Scheduled & Unscheduled aircraft maintenance
Major & Minor repairs
STC installations
Aircraft Weight & Balance
Aircraft Painting
Aircraft Cleaning
Maintenance Tracking Utilizing Tracking Programs or spreadsheets
Removal & Installation of Components
Aircraft Pre Buy Inspections
Nice to have
• modern , sleek , aviation

Meet the Staff

Picture with Headset on flying in a helicopter

CEO Tobias Whitcombe

Tobias Has been an aircraft mechanic for over 10 years . He has worked for the largest sightseeing & charter tourism company in the New York City area as well as repair stations & manufacturers. He has aircraft specific training to the Corvane TQ820 & Tovrin 4K7. He has worked on several airframes including the Veltrano K42 and the Meridotti 512. He has held every position in an aircraft maintenance department from mechanic up to Director of Maintenance . His work ethic and ability to manage mechanics in a organized and structured way gives any department or inspection a clear direction .

About Us

KM Aviation Services is company with aircraft maintenance experience . We focus on inspections of aircraft . Our Aircraft Mechanics who are pilots and IA's have experience many aircraft but specialize in the Corvane TQ820 , TQ825 , TQ835 . The Veltrano K42 and Meridotti Halberk 512 . Our focus is safety and to maintain aircraft day in and day out so our customer can operate the aircraft safely while keeping up with all the manufacturers inspections .

We know aircraft maintenance & maintenance planning . Leave the technical and tedious things to us . Get in your aircraft and fly knowing you have the best maintenance crew in the business.

```html
<!DOCTYPE html>
<html lang="en">
<head>
<meta charset="utf-8">
<title>Contact | KM Aviation</title>
<link href="https://fonts.googleapis.com/css2?family=Orbitron:wght@600;700&family=Poppins:wght@400;500;600&family=Roboto:wght@400;500&display=swap" rel="stylesheet">
<style>
  :root {
    --blue: #1a47a0;
    --navy: #0f1c3a;
    --grey-field: #ececec;
    --text: #444;
    --nav-grey: #6b6b6b;
    --footer: #3b3b3d;
    --white: #fff;
  }
  * { box-sizing: border-box; margin: 0; padding: 0; }
  html, body { width: 750px; height: 1200px; overflow: hidden; }
  body { position: relative; background: var(--white); font-family: 'Roboto', sans-serif; color: var(--text); }
  .abs { position: absolute; }

  .site-header { left: 0; top: 0; width: 750px; height: 42px; background: var(--white); z-index: 3; }
  .brand { left: 56px; top: 10px; display: flex; align-items: center; gap: 5px; font-family: 'Poppins', sans-serif; font-weight: 600; font-size: 12px; color: var(--blue); }
  .brand-dot { width: 20px; height: 20px; border-radius: 50%; background: var(--blue); }
  .main-nav { right: 55px; top: 16px; display: flex; gap: 17px; align-items: center; font-family: 'Poppins', sans-serif; font-weight: 600; font-size: 8.3px; color: var(--nav-grey); }
  .main-nav .active { color: var(--blue); }

  .hero { left: 0; top: 42px; width: 750px; height: 230px; background: linear-gradient(120deg, #22346a 0%, #3d4a78 25%, #7a7e8c 45%, #8d8f98 55%, #233f8f 72%, #8f96aa 100%); }
  .hero-slant { left: 0; top: 190px; }
  .hero-title { left: 0; top: 105px; width: 750px; text-align: center; font-family: 'Orbitron', sans-serif; font-weight: 700; font-size: 38px; color: var(--white); letter-spacing: 1px; }
  .breadcrumb { left: 0; top: 150px; width: 750px; text-align: center; font-family: 'Poppins', sans-serif; font-weight: 600; font-size: 12.5px; color: var(--white); }

  .form-title { left: 67px; top: 337px; font-family: 'Orbitron', sans-serif; font-weight: 700; font-size: 24px; color: var(--navy); letter-spacing: .5px; }
  .form-intro { left: 67px; top: 371px; width: 300px; font-size: 10px; line-height: 15px; color: var(--text); }
  .field { background: var(--grey-field); font-family: 'Poppins', sans-serif; font-weight: 500; font-size: 8.6px; color: #555; padding: 10px 14px; }
  .submit { left: 68px; top: 604px; width: 87px; height: 29px; background: var(--blue); clip-path: polygon(0 0, 100% 0, 82% 100%, 0 100%); color: var(--white); font-family: 'Poppins', sans-serif; font-weight: 600; font-size: 10px; padding: 7px 0 0 18px; }

  .info-panel { left: 423px; top: 341px; width: 249px; height: 277px; background: var(--blue); color: var(--white); }
  .info-title { left: 35px; top: 60px; font-family: 'Orbitron', sans-serif; font-weight: 700; font-size: 19px; }
  .info-list { left: 35px; top: 90px; list-style: none; font-size: 13px; line-height: 22.3px; }
  .info-list li { display: flex; gap: 12px; }
  .info-list svg { flex: none; width: 13px; height: 13px; margin-top: 4px; fill: var(--white); }
  .social { display: flex; gap: 5px; }
  .social span { display: flex; align-items: center; justify-content: center; border-radius: 50%; background: var(--white); }
  .info-social { left: 35px; top: 206px; }
  .info-social span { width: 24px; height: 24px; }
  .info-social svg { width: 11px; height: 11px; fill: none; stroke: var(--navy); stroke-width: 1.6; }

  .photo { left: 0; top: 630px; width: 750px; height: 380px; background: linear-gradient(180deg, #fff 0%, #e4e5e7 14%, #b8babe 32%, #8d8f93 46%, #6f7175 58%, #a1a3a6 66%, #7a7c80 78%, #55565a 90%, var(--footer) 100%); }
  .footer { left: 0; top: 1005px; width: 750px; height: 195px; background: var(--footer); color: #e8e8e8; font-family: 'Poppins', sans-serif; }
  .footer-brand { left: 56px; top: 60px; display: flex; align-items: center; gap: 8px; font-size: 20px; font-weight: 600; color: var(--white); }
  .footer-brand .brand-dot { width: 40px; height: 40px; }
  .f-head { top: 14px; font-family: 'Orbitron', sans-serif; font-weight: 600; font-size: 11.5px; color: var(--white); }
  .f-list { top: 32px; list-style: none; font-size: 9px; line-height: 16.7px; }
  .f-list li { display: flex; gap: 7px; align-items: center; }
  .f-list svg { width: 7px; height: 7px; fill: #aaa; }
  .news-input { left: 394px; top: 49px; width: 138px; height: 24px; background: #4d4d50; font-size: 7.5px; color: #ccc; padding: 6px 9px; }
  .news-btn { left: 394px; top: 76px; width: 72px; height: 20px; background: var(--blue); clip-path: polygon(0 0, 100% 0, 86% 100%, 0 100%); font-size: 7.5px; font-weight: 600; color: var(--white); padding: 4px 0 0 10px; }
  .f-social { left: 567px; top: 86px; }
  .f-social span { width: 17px; height: 17px; background: #555558; }
  .f-social svg { width: 8px; height: 8px; fill: none; stroke: #fff; stroke-width: 1.6; }
  .divider { left: 56px; top: 161px; width: 638px; height: 1px; background: #5a5a5d; }
  .copyright { left: 0; top: 171px; width: 750px; text-align: center; font-size: 8px; font-weight: 500; color: var(--white); }
  .to-top { left: 706px; top: 151px; width: 20px; height: 20px; border-radius: 50%; background: var(--blue); }
</style>
</head>
<body>
  <header class="site-header abs">
    <div class="brand abs"><span class="brand-dot"></span>KM Aviation</div>
    <nav class="main-nav abs">
      <svg width="10" height="9" viewBox="0 0 10 9"><path d="M5 0 0 4.5h1.3V9h2.7V6h2v3h2.7V4.5H10z" fill="#6b6b6b"/></svg>
      <span>AIRCRAFT MAINTENANCE</span><span>AIRCRAFT CLEANING</span><span>ABOUT US</span><span>CAREERS</span><span class="active">CONTACT</span>
    </nav>
  </header>

  <section class="hero abs" role="img" aria-label="Close-up photo of a helicopter engine bay under maintenance"></section>
  <svg class="hero-slant abs" width="750" height="82" viewBox="0 0 750 82">
    <polygon points="0,58 600,15 750,4 750,82 0,82" fill="#1a47a0"/>
    <polygon points="0,82 750,4 750,82" fill="#fff"/>
  </svg>
  <h1 class="hero-title abs">CONTACT</h1>
  <p class="breadcrumb abs">Home / Contact</p>

  <h2 class="form-title abs">SEND US A MESSAGE</h2>
  <p class="form-intro abs">Have an upcoming project that you want to discuss with us? Just fill out the form below and we’ll contact you back soon.</p>
  <div class="field abs" style="left:66px;top:412px;width:160px;height:30px">First name</div>
  <div class="field abs" style="left:233px;top:412px;width:159px;height:30px">Last name</div>
  <div class="field abs" style="left:66px;top:448px;width:160px;height:31px">Phone number</div>
  <div class="field abs" style="left:233px;top:448px;width:159px;height:31px">Email address</div>
  <div class="field abs" style="left:67px;top:486px;width:325px;height:112px;padding-top:12px">Message</div>
  <div class="submit abs">SUBMIT</div>

  <aside class="info-panel abs">
    <h3 class="info-title abs">CONTACT INFO</h3>
    <ul class="info-list abs">
      <li><svg viewBox="0 0 12 16"><path d="M6 0a6 6 0 0 0-6 6c0 4.5 6 10 6 10s6-5.5 6-10a6 6 0 0 0-6-6zm0 8.5A2.5 2.5 0 1 1 6 3.5a2.5 2.5 0 0 1 0 5z"/></svg><span>1234 W. 00th St. #133<br>Street, CA 12345</span></li>
      <li><svg viewBox="0 0 14 14"><rect x="3" y="0" width="8" height="4"/><rect x="0" y="5" width="14" height="6" rx="1"/><rect x="3" y="9" width="8" height="5"/></svg><span>(310) 123-4567</span></li>
      <li><svg viewBox="0 0 14 14"><path d="M3 0 0 2c0 6 6 12 12 12l2-3-3-2-2 1.5C7 9.5 4.5 7 3.5 5L5 3z"/></svg><span>(310) 123-4567</span></li>
      <li><svg viewBox="0 0 14 14"><path d="M0 2h14v1.5L7 8 0 3.5zM0 5l7 4.5L14 5v7H0z"/></svg><span>info@example.com</span></li>
    </ul>
    <div class="social info-social abs">
      <span aria-label="Share"><svg viewBox="0 0 12 12"><circle cx="3" cy="6" r="1.6"/><circle cx="9" cy="2.5" r="1.6"/><circle cx="9" cy="9.5" r="1.6"/><path d="M4.4 5.2 7.6 3.3M4.4 6.8l3.2 1.9"/></svg></span>
      <span aria-label="Message"><svg viewBox="0 0 12 12"><path d="M1.5 2h9v6h-5l-3 2.5V8h-1z"/></svg></span>
      <span aria-label="Website"><svg viewBox="0 0 12 12"><circle cx="6" cy="6" r="4.5"/><path d="M1.5 6h9M6 1.5c-2.4 3-2.4 6 0 9M6 1.5c2.4 3 2.4 6 0 9"/></svg></span>
    </div>
  </aside>

  <section class="photo abs" role="img" aria-label="Black and white photo of a twin-engine helicopter parked on a wet apron in front of a hangar"></section>

  <footer class="footer abs">
    <div class="footer-brand abs"><span class="brand-dot"></span>KM Aviation</div>
    <h4 class="f-head abs" style="left:250px">USEFUL LINKS</h4>
    <ul class="f-list abs" style="left:251px">
      <li>Home</li><li>Aircraft Maintenance</li><li>Aircraft Cleaning</li><li>About Us</li><li>Careers</li><li>Contact</li>
    </ul>
    <h4 class="f-head abs" style="left:394px">NEWSLETTER</h4>
    <ul class="f-list abs" style="left:393px"><li>Subscribe to our newsletter</li></ul>
    <div class="news-input abs">Email Address</div>
    <div class="news-btn abs">SUBSCRIBE</div>
    <h4 class="f-head abs" style="left:567px">CONTACT US</h4>
    <ul class="f-list abs" style="left:567px">
      <li><svg viewBox="0 0 12 16"><path d="M6 0a6 6 0 0 0-6 6c0 4.5 6 10 6 10s6-5.5 6-10a6 6 0 0 0-6-6z"/></svg>Some goes address here</li>
      <li><svg viewBox="0 0 14 14"><path d="M0 2h14v1.5L7 8 0 3.5zM0 5l7 4.5L14 5v7H0z"/></svg>info@email.com</li>
      <li><svg viewBox="0 0 14 14"><path d="M3 0 0 2c0 6 6 12 12 12l2-3-3-2-2 1.5C7 9.5 4.5 7 3.5 5L5 3z"/></svg>+124 4885 585</li>
    </ul>
    <div class="social f-social abs">
      <span aria-label="Share"><svg viewBox="0 0 12 12"><circle cx="3" cy="6" r="1.6"/><circle cx="9" cy="2.5" r="1.6"/><circle cx="9" cy="9.5" r="1.6"/><path d="M4.4 5.2 7.6 3.3M4.4 6.8l3.2 1.9"/></svg></span>
      <span aria-label="Message"><svg viewBox="0 0 12 12"><path d="M1.5 2h9v6h-5l-3 2.5V8h-1z"/></svg></span>
      <span aria-label="Website"><svg viewBox="0 0 12 12"><circle cx="6" cy="6" r="4.5"/><path d="M1.5 6h9M6 1.5v9"/></svg></span>
      <span aria-label="Link"><svg viewBox="0 0 12 12"><path d="M5 7l2-2M4 5.5 2.5 7a1.8 1.8 0 0 0 2.5 2.5L6.5 8M8 6.5 9.5 5A1.8 1.8 0 0 0 7 2.5L5.5 4"/></svg></span>
    </div>
    <div class="divider abs"></div>
    <p class="copyright abs">Copyright 2020 | All Rights Reserved</p>
    <div class="to-top abs"><svg width="20" height="20" viewBox="0 0 20 20"><path d="M7 11.5 10 8.5l3 3" stroke="#fff" stroke-width="1.4" fill="none"/></svg></div>
  </footer>
</body>
</html>
```